Turning Lecture Halls into Studios of Bold Discovery

This is for a book cover aimed at professors in higher education who want to infuse creative thinking into their classroom. It should have the title on the cover (see name of project). Our first idea is to have a stack of academic type books on a desk in black and white and then have a colorful rainbow light thread hitting the books. However, we are open to options! It has to be sophisticated, cool, and creative ;)

Target Market(s)

Higher Education Instructors

Industry/Entity Type

education

Font styles to use
Serif
Sans Serif

Requirements
Nice to have
• a creative feel of some sort
Should not have
• lightbulbs

```html
<!DOCTYPE html>
<html lang="en">
<head>
<meta charset="utf-8">
<title>Turning Lecture Halls into Studios of Bold Discovery — Book Cover</title>
<link rel="stylesheet" href="https://fonts.googleapis.com/css2?family=Playfair+Display:wght@500;600&family=Great+Vibes&family=Josefin+Sans:wght@400&display=swap">
<style>
  :root {
    --backdrop: #4d72bd;
    --cover-paper: #f7f6f3;
    --ink-navy: #1b3b7e;
    --rule-navy: #2c4a8a;
    --ray-rose: #f2b3bd;
    --ray-peach: #f5cfa6;
    --ray-butter: #efe2a4;
    --ray-sage: #a9cbb1;
    --ray-sky: #a8cbe2;
    --ray-lilac: #c9bde2;
    --fan-ink: #4a4f57;
  }
  * { box-sizing: border-box; margin: 0; padding: 0; }
  html, body {
    width: 1200px;
    height: 1000px;
    overflow: hidden;
    background: var(--backdrop);
  }
  .canvas {
    width: 1200px;
    height: 1000px;
    display: flex;
    align-items: center;
    justify-content: center;
  }
  .book-cover {
    position: relative;
    width: 620px;
    height: 930px;
    background: var(--cover-paper);
    box-shadow: 0 18px 40px rgba(20, 35, 80, 0.35);
    display: flex;
    flex-direction: column;
    align-items: center;
    overflow: hidden;
  }
  .title-block {
    margin-top: 62px;
    width: 100%;
    display: flex;
    flex-direction: column;
    align-items: center;
    color: var(--ink-navy);
    position: relative;
    z-index: 2;
  }
  .ruled-line {
    display: flex;
    align-items: center;
    gap: 18px;
  }
  .ruled-line::before,
  .ruled-line::after {
    content: "";
    display: block;
    height: 1.5px;
    background: var(--rule-navy);
  }
  .title-kicker::before,
  .title-kicker::after { width: 150px; }
  .title-connector::before,
  .title-connector::after { width: 90px; }
  .title-kicker span {
    font-family: "Playfair Display", serif;
    font-weight: 500;
    font-size: 26px;
    letter-spacing: 0.04em;
  }
  .title-main {
    font-family: "Playfair Display", serif;
    font-weight: 600;
    font-size: 92px;
    line-height: 0.92;
    text-align: center;
    letter-spacing: 0.005em;
    margin-top: 6px;
  }
  .title-connector { margin-top: 8px; }
  .title-connector span {
    font-family: "Great Vibes", cursive;
    font-size: 40px;
    line-height: 1;
  }
  .title-tail {
    font-family: "Playfair Display", serif;
    font-weight: 600;
    font-size: 40px;
    line-height: 1.05;
    text-align: center;
    margin-top: 4px;
  }
  .cover-art {
    position: absolute;
    left: 50%;
    top: 595px;
    width: 560px;
    height: 560px;
    transform: translate(-50%, -50%);
    border-radius: 50%;
    z-index: 1;
  }
  .cover-art .glow {
    position: absolute;
    inset: 0;
    border-radius: 50%;
    background: conic-gradient(from 20deg,
      var(--ray-peach), var(--ray-butter), var(--ray-sage), var(--ray-sky),
      var(--ray-lilac), var(--ray-rose), var(--ray-peach));
    filter: blur(40px);
    opacity: 0.55;
  }
  .cover-art .fan {
    position: absolute;
    left: 50%;
    top: 50%;
    width: 320px;
    height: 320px;
    transform: translate(-50%, -50%);
    border-radius: 50%;
    background:
      radial-gradient(circle, rgba(74, 79, 87, 0.75) 0 12%, rgba(74, 79, 87, 0.35) 55%, rgba(74, 79, 87, 0) 72%),
      conic-gradient(from 20deg,
        #d9b08f, #d8c98d, #7f927f, #6f7f8c, #6d6a7c, #c98b93, #d9b08f);
    filter: blur(2px);
  }
  .author-name {
    position: absolute;
    bottom: 56px;
    width: 100%;
    text-align: center;
    font-family: "Josefin Sans", sans-serif;
    font-weight: 400;
    font-size: 36px;
    letter-spacing: 0.18em;
    color: var(--ink-navy);
    z-index: 2;
  }
</style>
</head>
<body>
  <main class="canvas">
    <article class="book-cover">
      <header class="title-block">
        <div class="ruled-line title-kicker"><span>TURNING</span></div>
        <h1 class="title-main">LECTURE<br>HALLS</h1>
        <div class="ruled-line title-connector"><span>into Studios of</span></div>
        <p class="title-tail">BOLD<br>DISCOVERY</p>
      </header>

      <div class="cover-art" role="img" aria-label="Photograph of open books arranged in a circle, their rainbow-coloured spines and fanned pages radiating outward in soft light">
        <div class="glow"></div>
        <div class="fan"></div>
      </div>

      <p class="author-name">AUTHOR NAME</p>
    </article>
  </main>
</body>
</html>
```